CPA, Management and IT Consulting Redesign Existing Website

We currently have a website that is outdated (www.qelvarn.com). We need a good website developer that can redesign our website. To make this easier I have chosen a few websites that we like the layout or template. Use our exiting website content for this project. Our new logo is attached below. Based on who wins this we will upgrade to a coded website and a content management system (CMS) so we can make changes to the text ourselves in the future.

http://www.brontekhaile.com/
http://www.lorvicanmanagement.com/

Target Market(s)

Government Clients

Industry/Entity Type

Management Consulting

Number of Pages Required

5+ page

Font styles to use
Serif

Requirements
Must have
• Please the following website templates as a guide.
• http://www.brontekhaile.com/
• http://www.lorvicanmanagement.com/
Nice to have
Should not have

```html
<!DOCTYPE html>
<html lang="en">
<head>
<meta charset="utf-8">
<title>Corvell Enterprises, LLC</title>
<link rel="stylesheet" href="https://fonts.googleapis.com/css2?family=Lato:wght@400;700;900&display=swap">
<style>
:root{
  --orange:#f7931e;
  --orange-dark:#e07b0c;
  --ink:#1a1a1a;
  --text:#333;
  --muted:#555;
  --band:#efefef;
  --white:#fff;
  --footer:#141414;
  --navy:#1f2a44;
}
*{box-sizing:border-box;margin:0;padding:0}
html,body{width:1200px;height:2707px;overflow:hidden}
body{position:relative;font-family:"Lato",Arial,sans-serif;color:var(--text);background:var(--white)}
.abs{position:absolute}

/* header */
.brand{left:108px;top:32px;display:flex;align-items:center;gap:14px;width:360px}
.brand-mark{width:60px;height:72px;background:var(--orange);flex:none}
.brand-name{font-size:27px;font-weight:900;color:var(--ink);line-height:29px;white-space:nowrap}
.brand-name small{display:block;font-size:8.5px;font-weight:900;letter-spacing:.6px;line-height:10px;margin-top:3px;color:var(--ink)}
.top-contact{top:24px;right:110px;display:flex;gap:30px;font-size:16px;color:var(--ink);align-items:center}
.top-contact span{display:flex;align-items:center;gap:10px}
.dot{width:28px;height:28px;border-radius:50%;background:var(--orange);display:inline-flex;align-items:center;justify-content:center}
.main-nav{top:72px;right:108px;display:flex;gap:8px;font-size:14px;font-weight:700;color:var(--ink)}
.main-nav a{padding:8px 16px;text-decoration:none;color:inherit}
.main-nav a.active{background:var(--ink);color:var(--white)}

/* hero */
.hero{left:0;top:126px;width:1200px;height:520px;background:linear-gradient(120deg,#9cc6e4 0%,#4d8fc0 40%,#1d5d92 75%,#0f3d66 100%)}
.hero-caption{left:0;bottom:0;width:100%;height:90px;background:rgba(20,30,40,.78);color:var(--white);font-size:27px;text-align:center;line-height:38px;padding-top:8px}
.arrow{top:230px;width:30px;height:60px}

/* section titles */
.title{left:0;width:1200px;text-align:center;font-size:29px;font-weight:700;color:var(--ink)}
.title em{font-style:normal;color:var(--orange)}
.rule{left:50%;width:520px;margin-left:-260px;height:2px;background:#bbb}
.rule::after{content:"";position:absolute;left:50%;top:-4px;width:8px;height:10px;margin-left:-4px;background:#666}

.welcome-text{left:108px;top:768px;width:984px;font-size:14.5px;line-height:23px;text-align:center;color:var(--text)}
.btn{background:var(--orange);color:var(--white);font-weight:700;text-align:center;border-radius:2px}
.read-more{left:543px;top:890px;width:117px;height:35px;line-height:35px;font-size:14px}

/* services */
.services{left:0;top:975px;width:1200px;height:430px;background:var(--band)}
.service{top:1115px;width:230px;text-align:center}
.service svg{display:block;margin:0 auto}
.service h3{margin-top:30px;font-size:21px;font-weight:700;color:var(--ink);line-height:26px}
.service.active h3{color:var(--orange)}
.service p{margin-top:12px;font-size:16px;line-height:23px;color:var(--muted)}
.service p b{color:var(--orange);font-weight:400}
.divider{top:1150px;width:1px;height:200px;background:#d6d6d6}

/* consulting */
.consult{left:108px;top:1455px;width:984px;height:312px;background:var(--navy)}
.consult-photo{right:0;top:0;width:440px;height:312px;background:linear-gradient(90deg,#2b3350 0%,#d9d3c6 35%,#ece7dc 100%)}
.consult h2{left:35px;top:62px;font-size:40px;font-weight:400;color:var(--white)}
.consult p{left:35px;top:118px;font-size:21px;line-height:30px;color:var(--white)}
.consult .btn{left:35px;top:197px;width:223px;height:40px;line-height:40px;font-size:20px}

/* industries */
.industries{left:0;top:1820px;width:1200px;height:472px;background:var(--band)}
.tile{width:224px;height:145px;background:var(--white);text-align:center;padding-top:20px}
.tile .ic{width:58px;height:58px;border-radius:50%;background:#e6e6e6;margin:0 auto;display:flex;align-items:center;justify-content:center}
.tile p{margin-top:12px;font-size:13px;line-height:16px;color:var(--ink)}
.tile-hub{left:317px;top:2070px;width:44px;height:44px;border-radius:50%;background:var(--band)}
.video{left:670px;top:1948px;width:418px;height:294px;background:linear-gradient(110deg,#8fa5b8 0%,#c7ccd0 45%,#6f7d8c 100%)}
.video-bar{left:0;bottom:0;width:100%;height:22px;background:#111}

/* clients */
.clients-label{left:108px;top:2340px;font-size:27px;font-weight:700;line-height:30px;color:var(--ink)}
.clients-label em{font-style:normal;color:var(--orange);display:block}
.badge{top:2343px;height:61px;border:1px solid #e2e2e2;background:#f7f7f7}

/* footer */
.footer{left:0;top:2455px;width:1200px;height:207px;background:var(--footer);color:var(--white)}
.foot-nav{left:162px;top:31px;display:flex;align-items:center;gap:30px;font-size:14px}
.foot-nav i{width:6px;height:6px;background:var(--orange);display:inline-block}
.foot-mark{left:924px;top:32px;width:145px;height:152px;background:#2a2a2a}
.foot-addr{left:108px;top:102px;font-size:14px;line-height:20px}
.foot-addr b{font-weight:900}
.foot-contact{left:412px;top:102px;font-size:14px;line-height:28px}
.foot-contact span{display:flex;align-items:center;gap:12px}
.email{left:646px;top:103px;width:195px;height:32px;border:1px solid #ccc;background:var(--footer);color:var(--white);font-size:12px;line-height:30px;padding-left:8px}
.submit{left:646px;top:146px;width:195px;height:31px;line-height:31px;font-size:15px}
.bottom-bar{left:0;top:2662px;width:1200px;height:45px;background:var(--orange);color:var(--white);font-size:13px;line-height:45px;padding-left:108px}
.social{right:108px;top:8px;display:flex;gap:8px}
.social i{width:29px;height:29px;border-radius:50%;background:var(--white);opacity:.9;display:block}
</style>
</head>
<body>

<header>
  <div class="abs brand">
    <div class="brand-mark"></div>
    <div class="brand-name">CORVELL<br>ENTERPRISES, LLC<small>CONSULTANTS AND CERTIFIED PUBLIC ACCOUNTANTS</small></div>
  </div>
  <div class="abs top-contact">
    <span><i class="dot"><svg width="14" height="14" viewBox="0 0 24 24"><path fill="#fff" d="M6.6 10.8a15 15 0 006.6 6.6l2.2-2.2c.3-.3.7-.4 1-.2 1.1.4 2.3.6 3.6.6.6 0 1 .4 1 1V20c0 .6-.4 1-1 1C10.6 21 3 13.4 3 4c0-.6.4-1 1-1h3.5c.6 0 1 .4 1 1 0 1.3.2 2.5.6 3.6.1.3 0 .7-.2 1z"/></svg></i>(202) 555-0148</span>
    <span><i class="dot"><svg width="14" height="12" viewBox="0 0 24 18"><rect x="1" y="1" width="22" height="16" fill="#fff"/><path d="M1 1l11 9 11-9" stroke="#f7931e" stroke-width="2" fill="none"/></svg></i>info@qelvarn.com</span>
  </div>
  <nav class="abs main-nav">
    <a class="active">HOME</a><a>ABOUT US</a><a>SERVICES</a><a>INDUSTRIES</a><a>CONTACT US</a>
  </nav>
</header>

<section class="abs hero" role="img" aria-label="Hand touching a digital interface with world map and data panels in blue tones">
  <svg class="abs arrow" style="left:52px" viewBox="0 0 30 60"><path d="M24 6L6 30l18 24" stroke="#fff" stroke-width="4" fill="none"/></svg>
  <svg class="abs arrow" style="right:52px" viewBox="0 0 30 60"><path d="M6 6l18 24-18 24" stroke="#fff" stroke-width="4" fill="none"/></svg>
  <div class="abs hero-caption">We Are Committed To Professional Excellence Across All Service Areas Including Audit<br>&amp; Assurance, Accounting, Tax, Management Consulting, &amp; Information Technology</div>
</section>

<section>
  <h1 class="abs title" style="top:690px">WELCOME TO CORVELL <em>ENTERPRISES, LLC</em></h1>
  <div class="abs rule" style="top:738px"></div>
  <p class="abs welcome-text">Corvell Enterprises, LLC and Ashby &amp; Morrow, LLC is a network of certified public accounting and management consulting firms with seasoned professionals and an excellent reputation for serving a diverse client base including federal agencies, state and local government, non-profit organizations, small and medium-sized business entities, professional associations and individuals. We are committed to professional excellence across all service areas including Audit and Assurance, Accounting, Tax, Management Consulting, and Information Technology.</p>
  <div class="abs btn read-more">READ MORE</div>
</section>

<section class="abs services"></section>
<h2 class="abs title" style="top:1013px">OUR <em>SERVICES</em></h2>
<div class="abs rule" style="top:1058px;width:200px;margin-left:-100px"></div>

<div class="abs service active" style="left:105px">
  <svg width="90" height="90" viewBox="0 0 90 90" fill="none" stroke="#f7931e" stroke-width="3"><ellipse cx="30" cy="56" rx="18" ry="6"/><path d="M12 56v18c0 3 8 6 18 6s18-3 18-6V56M12 65c0 3 8 6 18 6s18-3 18-6"/><circle cx="50" cy="30" r="18"/><path d="M63 43l18 18"/></svg>
  <h3>Audit, Accounting<br>&amp; Tax</h3>
  <p>Lorem ipsum dolor sit amet, consectetuer adipis <b>...[+]</b></p>
</div>
<div class="abs divider" style="left:347px"></div>
<div class="abs service" style="left:360px">
  <svg width="90" height="90" viewBox="0 0 90 90"><g fill="#1a1a1a"><rect x="8" y="58" width="9" height="24"/><rect x="22" y="48" width="9" height="34"/><rect x="36" y="52" width="9" height="30"/><rect x="50" y="38" width="9" height="44"/><rect x="64" y="26" width="9" height="56"/><rect x="4" y="82" width="82" height="4"/></g><path d="M12 50l14-12 14 6 14-16 14-16" stroke="#1a1a1a" stroke-width="3" fill="none"/><g fill="#1a1a1a"><circle cx="12" cy="50" r="4"/><circle cx="26" cy="38" r="4"/><circle cx="40" cy="44" r="4"/><circle cx="54" cy="28" r="4"/><circle cx="68" cy="12" r="4"/></g></svg>
  <h3>Financial<br>Management</h3>
  <p>Lorem ipsum dolor sit amet, consectetuer adipis <b style="color:inherit">...[+]</b></p>
</div>
<div class="abs divider" style="left:600px"></div>
<div class="abs service" style="left:612px">
  <svg width="90" height="90" viewBox="0 0 90 90"><rect x="26" y="6" width="40" height="64" rx="4" fill="none" stroke="#1a1a1a" stroke-width="4"/><rect x="32" y="14" width="28" height="44" fill="#1a1a1a"/><path d="M46 58v-8c0-3 5-3 5 0v6l10 2c4 1 5 4 4 8l-3 18H44l-8-14c-2-4 2-6 5-3z" fill="#1a1a1a"/></svg>
  <h3>Information<br>Technology</h3>
  <p>Lorem ipsum dolor sit amet, consectetuer adipis <b style="color:inherit">...[+]</b></p>
</div>
<div class="abs divider" style="left:853px"></div>
<div class="abs service" style="left:865px">
  <svg width="90" height="90" viewBox="0 0 90 90" fill="#1a1a1a"><circle cx="45" cy="12" r="7"/><path d="M33 32c0-8 24-8 24 0z"/><circle cx="15" cy="60" r="7"/><path d="M3 80c0-8 24-8 24 0z"/><circle cx="75" cy="60" r="7"/><path d="M63 80c0-8 24-8 24 0z"/><path d="M45 36v14M45 50L22 56M45 50l23 6" stroke="#1a1a1a" stroke-width="3" stroke-dasharray="4 3" fill="none"/></svg>
  <h3>Governance, Risk<br>&amp; Compliance</h3>
  <p>Lorem ipsum dolor sit amet, consectetuer adipis <b style="color:inherit">...[+]</b></p>
</div>

<section class="abs consult">
  <div class="abs consult-photo" role="img" aria-label="Overhead view of a business team meeting around a table with laptops"></div>
  <h2 class="abs">CONSULTING SERVICE</h2>
  <p class="abs">We Are Providing Wide Range Of Consulting Services<br>&amp; World Wide Happy Clients</p>
  <div class="abs btn">CONTACT US TODAY</div>
</section>

<section class="abs industries"></section>
<h2 class="abs title" style="top:1854px">INDUSTRIES WE <em>WORK WITH</em></h2>
<div class="abs rule" style="top:1898px;width:400px;margin-left:-200px"></div>

<div class="abs tile" style="left:108px;top:1944px">
  <div class="ic"><svg width="32" height="32" viewBox="0 0 32 32" fill="#1a1a1a"><path d="M16 2L2 9h28z"/><rect x="5" y="11" width="3" height="13"/><rect x="11" y="11" width="3" height="13"/><rect x="18" y="11" width="3" height="13"/><rect x="24" y="11" width="3" height="13"/><rect x="2" y="26" width="28" height="4"/></svg></div>
  <p>FEDERAL<br>GOVERNMENT</p>
</div>
<div class="abs tile" style="left:345px;top:1944px">
  <div class="ic"><svg width="32" height="32" viewBox="0 0 32 32" fill="#1a1a1a"><rect x="15" y="1" width="2" height="5"/><path d="M8 14a8 8 0 0116 0z"/><rect x="6" y="15" width="20" height="3"/><rect x="7" y="19" width="2" height="7"/><rect x="12" y="19" width="2" height="7"/><rect x="18" y="19" width="2" height="7"/><rect x="23" y="19" width="2" height="7"/><rect x="3" y="27" width="26" height="4"/></svg></div>
  <p>STATE &amp; LOCAL<br>GOVERNMENT</p>
</div>
<div class="abs tile" style="left:108px;top:2101px">
  <div class="ic"><svg width="32" height="32" viewBox="0 0 32 32" fill="#1a1a1a"><rect x="3" y="20" width="20" height="4"/><rect x="3" y="25" width="20" height="4"/><rect x="9" y="6" width="20" height="12" rx="1"/><circle cx="19" cy="12" r="3" fill="#e6e6e6"/></svg></div>
  <p>FINANCIAL<br>SERVICES</p>
</div>
<div class="abs tile" style="left:345px;top:2101px">
  <div class="ic"><svg width="34" height="30" viewBox="0 0 34 30" fill="#1a1a1a"><path d="M1 8l7-4 7 4 5-3 6 1 7 4-3 8-5 5c-2 2-4 1-5 0l-2 2c-1 1-3 1-4 0L4 17z"/></svg></div>
  <p>NOT-FOR<br>PROFIT</p>
</div>
<div class="abs tile-hub"></div>

<div class="abs video" role="img" aria-label="Video still of colleagues meeting in an office">
  <div class="abs video-bar">
    <svg width="418" height="22" viewBox="0 0 418 22"><rect x="10" y="7" width="3" height="8" fill="#fff"/><rect x="15" y="7" width="3" height="8" fill="#fff"/><rect x="30" y="10" width="280" height="2" fill="#555"/><rect x="30" y="10" width="150" height="2" fill="#2d8fd6"/><circle cx="180" cy="11" r="4" fill="#fff"/><rect x="320" y="7" width="10" height="8" fill="#888"/><rect x="345" y="10" width="50" height="2" fill="#777"/><circle cx="372" cy="11" r="6" fill="#ddd"/></svg>
  </div>
</div>

<section>
  <h2 class="abs clients-label">OUR<em>CLIENTS</em></h2>
  <div class="abs badge" style="left:256px;width:145px"></div>
  <div class="abs badge" style="left:448px;width:177px"></div>
  <div class="abs badge" style="left:671px;width:192px"></div>
  <div class="abs badge" style="left:906px;width:173px"></div>
</section>

<footer class="abs footer">
  <nav class="abs foot-nav"><span>HOME</span><i></i><span>ABOUT US</span><i></i><span>SERVICES</span><i></i><span>INDUSTRIES</span><i></i><span>CONTACT US</span></nav>
  <div class="abs foot-mark"></div>
  <address class="abs foot-addr" style="font-style:normal"><b>CORVELL ENTERPRISES, LLC</b><br>2417 Larkmoor Street NW,<br>Suite 300 Washington,<br>DC 20009</address>
  <div class="abs foot-contact">
    <span><svg width="14" height="14" viewBox="0 0 24 24"><path fill="#f7931e" d="M6.6 10.8a15 15 0 006.6 6.6l2.2-2.2c.3-.3.7-.4 1-.2 1.1.4 2.3.6 3.6.6.6 0 1 .4 1 1V20c0 .6-.4 1-1 1C10.6 21 3 13.4 3 4c0-.6.4-1 1-1h3.5c.6 0 1 .4 1 1 0 1.3.2 2.5.6 3.6.1.3 0 .7-.2 1z"/></svg>(202) 555-0148</span>
    <span><svg width="14" height="14" viewBox="0 0 24 24" fill="#f7931e"><rect x="6" y="2" width="12" height="6"/><rect x="2" y="9" width="20" height="9" rx="2"/><rect x="6" y="15" width="12" height="7"/></svg>(202) 555-0193</span>
    <span><svg width="14" height="11" viewBox="0 0 24 18"><rect x="1" y="1" width="22" height="16" fill="#f7931e"/><path d="M1 1l11 9 11-9" stroke="#141414" stroke-width="2" fill="none"/></svg>info@qelvarn.com</span>
  </div>
  <div class="abs email">Enter Your Email Here</div>
  <div class="abs btn submit">SUBMIT</div>
</footer>

<div class="abs bottom-bar">Copyright © 2016 Corvell Enterprises, LLC. All Rights Reserved.
  <div class="abs social"><i></i><i></i><i></i><i></i></div>
</div>

</body>
</html>
```